Need UI design for an iOS app game with most of the layout planned

The name of the game is "QUADRIX".

The goal of the game is to find a way to manipulate four numbers so that the end result is 24. Addition, subtraction, multiplication and division may be used and each number can only be used once.

The list of items we need is:

1. launch image, app icon, UI design of all scenes (10-12 scenes) of the app.
2. App background image should support screen size of both 640x1136.
3. Files are preferred to be in (.eps) format so that resolution can be adjusted later. But other file formats are welcome as long as resolution is high enough.
4. Icons, buttons, background image etc. should have their own file so that later they can be moved around in case design is changed.

The detailed requirement is in the attached file. The actual layout can vary if it can help achieve better result. We also attached several screenshots from iOS game "Glimbo". You can use that as your reference.

```html
<!DOCTYPE html>
<html lang="en">
<head>
<meta charset="utf-8">
<title>QUADRIX – Single Player</title>
<link rel="stylesheet" href="https://fonts.googleapis.com/css2?family=Fredoka:wght@500;600;700&family=Lilita+One&family=Inter:wght@500;600&display=swap">
<style>
  :root {
    --stage: #e7e2da;
    --status-bg: #050505;
    --status-text: #ffffff;
    --nav-top: #1e6fe0;
    --nav-bottom: #0a3a9e;
    --nav-edge: #062a78;
    --back-top: #3fb2f5;
    --back-bottom: #1a82dc;
    --title-top: #ffe24a;
    --title-bottom: #ff9a12;
    --title-edge: #a44a00;
    --coin-top: #ffc531;
    --coin-bottom: #f08c00;
    --coin-disc: #ffffff;
    --body-center: #5f95ee;
    --body-edge: #3161c6;
    --label: #f7ea1c;
    --mode-fill: #0b6fa1;
    --mode-edge: #1a558a;
    --mode-text: #ffffff;
  }
  * { box-sizing: border-box; margin: 0; padding: 0; }
  html, body { width: 1200px; height: 900px; overflow: hidden; background: var(--stage); }
  .stage { position: relative; width: 1200px; height: 900px; }

  .screen {
    position: absolute; left: 375px; top: 50px;
    width: 450px; height: 800px; overflow: hidden;
    background: radial-gradient(ellipse 75% 55% at 50% 45%, var(--body-center), var(--body-edge));
    box-shadow: 0 10px 30px rgba(0,0,0,.18);
  }

  .status-bar {
    position: absolute; left: 0; top: 0; width: 100%; height: 27px;
    background: var(--status-bg); color: var(--status-text);
    font: 600 15px/27px "Inter", sans-serif;
  }
  .status-left { position: absolute; left: 8px; top: 0; display: flex; align-items: center; height: 27px; gap: 5px; }
  .status-time { position: absolute; left: 0; width: 100%; text-align: center; }
  .status-right { position: absolute; right: 8px; top: 0; display: flex; align-items: center; height: 27px; gap: 6px; }

  .nav-bar {
    position: absolute; left: 0; top: 27px; width: 100%; height: 65px;
    background: linear-gradient(var(--nav-top), var(--nav-bottom));
    border-bottom: 2px solid var(--nav-edge);
  }
  .back-button {
    position: absolute; left: 14px; top: 12px; width: 76px; height: 40px;
  }
  .back-button svg { position: absolute; inset: 0; }
  .back-button span {
    position: relative; display: block; padding-left: 20px; line-height: 40px;
    font: 600 18px/40px "Fredoka", sans-serif; color: #fff;
  }
  .nav-title {
    position: absolute; left: 0; width: 100%; top: 14px; text-align: center;
    font: 400 28px/36px "Lilita One", sans-serif; letter-spacing: .5px;
    background: linear-gradient(var(--title-top), var(--title-bottom));
    -webkit-background-clip: text; background-clip: text; color: transparent;
    -webkit-text-stroke: 1px var(--title-edge);
  }
  .coin-badge {
    position: absolute; right: 15px; top: 12px; width: 84px; height: 40px;
    border-radius: 5px; background: linear-gradient(var(--coin-top), var(--coin-bottom));
    display: flex; align-items: center; gap: 8px; padding-left: 9px;
    font: 600 19px/40px "Fredoka", sans-serif; color: #fff;
  }
  .coin-disc {
    width: 24px; height: 24px; border-radius: 50%; background: var(--coin-disc);
    color: var(--coin-bottom); font: 700 15px/24px "Fredoka", sans-serif; text-align: center;
  }

  .mode-list { position: absolute; left: 35px; top: 168px; width: 380px; }
  .mode-group { margin-bottom: 37px; text-align: center; }
  .mode-label { font: 600 21px/28px "Fredoka", sans-serif; color: var(--label); }
  .mode-button {
    display: block; margin-top: 6px; width: 380px; height: 80px;
    background: var(--mode-fill); border: 2px solid var(--mode-edge); border-radius: 6px;
    box-shadow: inset 0 1px 0 rgba(255,255,255,.12);
    font: 700 28px/76px "Fredoka", sans-serif; color: var(--mode-text);
  }
</style>
</head>
<body>
<div class="stage">
  <main class="screen">
    <header class="status-bar">
      <div class="status-left">
        <svg width="32" height="8" viewBox="0 0 32 8" aria-hidden="true">
          <circle cx="4" cy="4" r="3.2" fill="#fff"/><circle cx="11" cy="4" r="3.2" fill="#fff"/><circle cx="18" cy="4" r="3.2" fill="#fff"/>
          <circle cx="25" cy="4" r="2.8" fill="none" stroke="#fff" stroke-width=".9"/>
        </svg>
        <svg width="15" height="12" viewBox="0 0 15 12" aria-hidden="true">
          <path d="M1 4.5a9 9 0 0 1 13 0M3.3 6.8a5.6 5.6 0 0 1 8.4 0" fill="none" stroke="#fff" stroke-width="1.6" stroke-linecap="round"/>
          <circle cx="7.5" cy="10" r="1.6" fill="#fff"/>
        </svg>
      </div>
      <div class="status-time">4:21 PM</div>
      <div class="status-right">
        <svg width="9" height="14" viewBox="0 0 9 14" aria-hidden="true">
          <path d="M1 4l6 6-3 3V1l3 3-6 6" fill="none" stroke="#fff" stroke-width="1.3"/>
        </svg>
        <span>100%</span>
        <svg width="30" height="13" viewBox="0 0 30 13" aria-hidden="true">
          <rect x=".6" y=".6" width="26" height="11.8" rx="2" fill="none" stroke="#fff" stroke-width="1.2"/>
          <rect x="2.5" y="2.5" width="22.2" height="8" rx="1" fill="#fff"/>
          <rect x="27.5" y="4" width="2" height="5" rx="1" fill="#fff"/>
        </svg>
      </div>
    </header>

    <nav class="nav-bar">
      <div class="back-button">
        <svg width="76" height="40" viewBox="0 0 76 40" aria-hidden="true">
          <defs>
            <linearGradient id="backFill" x1="0" y1="0" x2="0" y2="1">
              <stop offset="0" stop-color="#3fb2f5"/><stop offset="1" stop-color="#1a82dc"/>
            </linearGradient>
          </defs>
          <path d="M14 1H71a4 4 0 0 1 4 4V35a4 4 0 0 1-4 4H14L1 20Z" fill="url(#backFill)" stroke="#0d5fb4" stroke-width="1.2" stroke-linejoin="round"/>
        </svg>
        <span>Back</span>
      </div>
      <h1 class="nav-title">Single Player</h1>
      <div class="coin-badge"><span class="coin-disc">$</span><span>360</span></div>
    </nav>

    <section class="mode-list">
      <div class="mode-group">
        <p class="mode-label">Label 1</p>
        <span class="mode-button">Mode 1</span>
      </div>
      <div class="mode-group">
        <p class="mode-label">Label 2</p>
        <span class="mode-button">Mode 2</span>
      </div>
      <div class="mode-group">
        <p class="mode-label">Label 1</p>
        <span class="mode-button">Mode 3</span>
      </div>
    </section>
  </main>
</div>
</body>
</html>
```